Sales Website Design

Create a sales-oriented website to advertise turn-key solutions for providing infection control to senior housing operators. There are several items uploaded. The pdf should serve as your guide. The powerpoint presentation has additional information.

The idea is this is senior housing reimagined for infection control. The design should be sleek, clean, vibrant and energetic.

Our goal is to sell a turnkey solution for making buildings safer for residents, staff, and families.

Target Market(s)

People who own and operate senior housing communities

```html
<!DOCTYPE html>
<html lang="en">
<head>
<meta charset="utf-8">
<title>Haven Guard — Senior Living Centered on Safety</title>
<link href="https://fonts.googleapis.com/css2?family=Roboto:wght@400;500;700;900&display=swap" rel="stylesheet">
<style>
:root{
  --orange:#f2521c;
  --orange-light:#f57a3c;
  --ink:#222629;
  --text:#4a4f54;
  --muted:#8a9096;
  --line:#d6d9dc;
  --white:#ffffff;
  --teal-dark:#2d4347;
  --teal:#40595d;
  --slate:#3a3d40;
  --foot-dark:#1f2a2e;
}
*{box-sizing:border-box;margin:0;padding:0}
html,body{width:1200px;height:4436px;overflow:hidden}
body{font-family:"Roboto",Arial,sans-serif;color:var(--text);background:var(--white);position:relative}
.abs{position:absolute}

/* header */
.site-header{left:0;top:0;width:1200px;height:80px;background:var(--white);z-index:2;display:flex;align-items:center;justify-content:space-between;padding:0 110px 0 110px}
.brand{font-weight:700;font-size:26px;color:var(--ink);display:flex;align-items:center;gap:10px}
.brand-dot{width:12px;height:12px;background:var(--orange)}
.main-nav{display:flex;gap:44px;font-size:17px;color:var(--ink)}
.main-nav .active{color:var(--orange);border-bottom:2px solid var(--orange);padding-bottom:6px}

/* hero */
.hero{left:0;top:80px;width:1200px;height:560px;background:linear-gradient(180deg,#9fb0c2 0%,#7c8c9b 40%,#5d6a55 80%,#4c5a3d 100%)}
.hero-title{left:0;top:280px;width:1200px;text-align:center;color:var(--white);font-weight:700;font-size:42px;line-height:50px;text-shadow:0 2px 6px rgba(0,0,0,.45)}
.hero-dots{left:566px;top:610px;display:flex;gap:22px}
.hero-dots span{width:10px;height:10px;border-radius:50%;background:rgba(255,255,255,.6)}
.hero-dots span:first-child{background:var(--white)}

/* about */
.about-photo{left:112px;top:780px;width:440px;height:332px;background:linear-gradient(135deg,#e9ecef,#b8c0c8 60%,#6d7680);border:4px solid #cfe0ee}
.about-title{left:608px;top:778px;font-size:38px;font-weight:700;letter-spacing:4px;color:var(--ink)}
.about-text{left:608px;top:846px;width:520px;font-size:15px;line-height:27px;color:var(--text)}
.btn{background:var(--orange);color:var(--white);font-weight:700;border-radius:30px;text-align:center}
.about-btn{left:608px;top:1064px;width:132px;height:40px;line-height:40px;font-size:15px}

/* benefits */
.benefits{left:0;top:1212px;width:1200px;height:548px;background:linear-gradient(180deg,var(--teal) 0%,var(--teal-dark) 100%)}
.section-title-light{color:var(--white);font-weight:700;font-size:40px;letter-spacing:2px;text-align:center;width:1200px;left:0}
.benefits-note{left:0;top:1318px;width:1200px;text-align:center;color:var(--white);font-size:19px;line-height:30px}
.benefit-card{top:1440px;width:220px;height:260px;background:rgba(255,255,255,.22);color:var(--white);text-align:center}
.benefit-card svg{position:absolute;left:80px;top:52px}
.benefit-card p{position:absolute;left:0;bottom:48px;width:100%;font-size:22px}
.vdots{display:flex;flex-direction:column;gap:8px}
.vdots span{width:8px;height:8px;border-radius:50%;background:var(--white)}

/* touchless */
.section-title{left:0;width:1200px;text-align:center;font-size:38px;font-weight:700;color:var(--ink);letter-spacing:2px}
.option-card{width:316px;height:308px;background:var(--white);border:1px solid var(--line);box-shadow:0 2px 6px rgba(0,0,0,.15)}
.option-card .ph{position:absolute;left:0;top:0;width:100%;height:254px}
.option-card p{position:absolute;left:0;bottom:0;width:100%;height:54px;line-height:54px;text-align:center;font-size:20px;color:var(--ink)}

/* technology */
.technology{left:0;top:2720px;width:1200px;height:592px;background:linear-gradient(180deg,#4b4e51,#2f3134)}
.tech-note{left:0;top:2848px;width:1200px;text-align:center;color:var(--white);font-size:17px;line-height:26px}
.tech-card{top:2952px;width:276px;height:296px;background:var(--white)}
.tech-card .ph{position:absolute;left:0;top:0;width:100%;height:196px}
.tech-card p{position:absolute;left:0;top:216px;width:100%;text-align:center;font-size:16px;font-weight:700;letter-spacing:2px;line-height:26px;color:var(--ink)}

/* contact form */
.field{border:1px solid var(--line);font-size:14px;letter-spacing:1px;color:var(--ink);padding:20px 24px;font-weight:500}
.send-btn{left:508px;top:3872px;width:140px;height:56px;line-height:56px;font-size:18px;letter-spacing:2px}

/* footer */
.site-footer{left:0;top:4012px;width:1200px;height:424px;background:linear-gradient(90deg,var(--foot-dark) 0%,#2c2a2a 45%,#b33d17 80%,var(--orange) 100%);color:var(--white)}
.foot-title{font-size:24px;font-weight:700;letter-spacing:2px}
.foot-text{font-size:15px;line-height:24px}
.social{display:flex;gap:14px}
.social span{width:34px;height:34px;border-radius:50%;border:2px solid var(--white)}
.contact-row{display:flex;align-items:flex-start;gap:22px;font-size:15px;line-height:24px}
.contact-icon{flex:0 0 34px;width:34px;height:34px;border-radius:50%;background:var(--orange);display:flex;align-items:center;justify-content:center}
.news-input{left:780px;top:4252px;width:300px;height:56px;background:var(--white);color:var(--ink);font-size:15px;line-height:56px;padding-left:20px}
.news-btn{left:1080px;top:4252px;width:60px;height:56px;background:var(--orange);display:flex;align-items:center;justify-content:center}
.copyright{left:0;top:4378px;width:1200px;text-align:center;font-size:12px;color:rgba(255,255,255,.8)}
</style>
</head>
<body>

<header class="site-header abs">
  <div class="brand">Haven Guard</div>
  <nav class="main-nav">
    <span class="active">Home</span><span>About Us</span><span>Benefits</span><span>Marketing</span><span>Process</span><span>Contact</span>
  </nav>
</header>

<section class="hero abs" role="img" aria-label="Photo of a two-storey suburban senior living home with lawn and garage"></section>
<h1 class="hero-title abs">Haven Guard for<br>Senior Living Communities Centered on Safety &amp;<br>Efficiency</h1>
<div class="hero-dots abs"><span></span><span></span></div>

<div class="about-photo abs" role="img" aria-label="Photo of a bright open-plan dining and kitchen area"></div>
<h2 class="about-title abs">ABOUT US</h2>
<p class="about-text abs">While the recent pandemic has gripped the world in recent months, it has disproportionately impacted the health of senior living residents and care givers and illuminated the vast importance of prioritizing safety for this population. Many studies report over 40% of the coronavirus related fatalities in the United States have occurred in a nursing home setting, driving an unwarranted negative perception of the sector.</p>
<div class="btn about-btn abs">READ MORE</div>

<section class="benefits abs"></section>
<h2 class="section-title-light abs" style="top:1256px">BENEFITS</h2>
<p class="benefits-note abs">Does NOT have to be circles! Could be tabs or some other element<br>I am envisioning you click on each topic then the benefits appear. The benefits are on the next slide.</p>

<div class="benefit-card abs" style="left:112px">
  <svg width="60" height="70" viewBox="0 0 60 70" fill="none" stroke="#fff" stroke-width="3"><rect x="8" y="6" width="26" height="60"/><rect x="34" y="26" width="18" height="40"/><path d="M15 16h12M15 28h12M15 40h12M15 52h12M40 36h6M40 48h6"/></svg>
  <p>Residents</p>
</div>
<div class="benefit-card abs" style="left:368px">
  <svg width="60" height="70" viewBox="0 0 60 70" fill="none" stroke="#fff" stroke-width="3"><circle cx="20" cy="20" r="8"/><circle cx="42" cy="24" r="7"/><path d="M6 50c0-10 6-16 14-16s14 6 14 16M30 52c0-8 5-14 12-14s12 6 12 14"/></svg>
  <p>Family &amp; Friends</p>
</div>
<div class="benefit-card abs" style="left:620px">
  <svg width="60" height="70" viewBox="0 0 60 70" fill="none" stroke="#fff" stroke-width="3"><circle cx="30" cy="18" r="9"/><path d="M12 60c0-14 8-22 18-22s18 8 18 22M30 38v10M24 44h12"/></svg>
  <p>Staff</p>
</div>
<div class="benefit-card abs" style="left:880px">
  <svg width="60" height="70" viewBox="0 0 60 70" fill="none" stroke="#fff" stroke-width="3"><circle cx="14" cy="24" r="6"/><circle cx="30" cy="20" r="7"/><circle cx="46" cy="24" r="6"/><path d="M4 52c0-9 4-14 10-14M56 52c0-9-4-14-10-14M18 54c0-11 5-17 12-17s12 6 12 17"/></svg>
  <p>Owners</p>
</div>
<div class="vdots abs" style="left:1136px;top:1512px"><span></span><span></span><span></span></div>

<h2 class="section-title abs" style="top:1848px">TOUCHLESS OPTIONS</h2>
<div class="option-card abs" style="left:104px;top:1972px"><div class="ph" role="img" aria-label="Photo of an automatic door opener" style="background:linear-gradient(135deg,#e6e2da,#a9a59c)"></div><p>Door openers</p></div>
<div class="option-card abs" style="left:432px;top:1972px"><div class="ph" role="img" aria-label="Photo of a row of light switches" style="background:linear-gradient(135deg,#3c3c3c,#d8d8d6 55%,#3a3a3a)"></div><p>Light switches</p></div>
<div class="option-card abs" style="left:760px;top:1972px"><div class="ph" role="img" aria-label="Photo of a touchless faucet" style="background:linear-gradient(135deg,#f2f4f6,#b9c0c6)"></div><p>Faucets</p></div>
<div class="option-card abs" style="left:104px;top:2320px"><div class="ph" role="img" aria-label="Photo of a towel dispenser on a wall" style="background:linear-gradient(135deg,#c9b8a4,#2b2b2b 60%,#b79b7e)"></div><p>Towel dispensers</p></div>
<div class="option-card abs" style="left:432px;top:2320px"><div class="ph" role="img" aria-label="Photo of wall-mounted soap dispensers" style="background:linear-gradient(135deg,#d9dde0,#5a6e74 60%,#c7cdd1)"></div><p>Soap dispensers</p></div>
<div class="option-card abs" style="left:760px;top:2320px"><div class="ph" role="img" aria-label="Photo of wall-hung touchless toilets" style="background:linear-gradient(135deg,#dcdfe2,#f4f5f6 50%,#a9afb4)"></div><p>Toilets</p></div>

<section class="technology abs" role="img" aria-label="Dimmed photo of a lounge interior as section background"></section>
<h2 class="section-title-light abs" style="top:2780px">TECHNOLOGY</h2>
<p class="tech-note abs">Haven Guard Technology Content Edits<br>We DO NOT want to use actual product shots. What can we do  instead</p>
<div class="tech-card abs" style="left:140px"><div class="ph" role="img" aria-label="Photo of a touchless temperature scanner in use" style="background:linear-gradient(135deg,#b7c6cf,#4d6573)"></div><p>TOUCHLESS<br>TEMPERATURE SCANS</p></div>
<div class="tech-card abs" style="left:464px"><div class="ph" role="img" aria-label="Photo of wireless diagnostic equipment" style="background:linear-gradient(135deg,#d8cfc5,#8c7b6c)"></div><p>WIRELESS DIAGNOSTIC<br>EQUIPMENT</p></div>
<div class="tech-card abs" style="left:784px"><div class="ph" role="img" aria-label="Photo of a wearable health monitoring device" style="background:linear-gradient(135deg,#e4e9e6,#9fb3a8)"></div><p>WEARABLE<br>MONITORING</p></div>
<div class="vdots abs" style="left:1084px;top:3060px"><span></span><span></span><span></span></div>

<h2 class="section-title abs" style="top:3396px">GET IN TOUCH</h2>
<div class="field abs" style="left:200px;top:3512px;width:364px;height:62px">FIRST NAME</div>
<div class="field abs" style="left:600px;top:3512px;width:368px;height:62px">LAST NAME</div>
<div class="field abs" style="left:200px;top:3600px;width:364px;height:62px">PHONE</div>
<div class="field abs" style="left:600px;top:3600px;width:368px;height:62px">BUSINESS</div>
<div class="field abs" style="left:200px;top:3692px;width:768px;height:140px">HOW CAN WE HELP?</div>
<div class="btn send-btn abs">SUBMIT</div>

<footer class="site-footer abs"></footer>
<div class="abs" style="left:100px;top:4072px">
  <div class="foot-title" style="letter-spacing:0">Haven Guard</div>
  <p class="foot-text" style="width:240px;margin-top:22px">Safer buildings, calmer residents, and confident staff through simple touchless upgrades</p>
  <div class="social" style="margin-top:30px"><span></span><span></span><span></span></div>
</div>
<div class="abs" style="left:412px;top:4072px">
  <div class="foot-title">CONTACT US</div>
  <div class="contact-row" style="margin-top:26px">
    <span class="contact-icon"><svg width="14" height="18" viewBox="0 0 14 18"><path d="M7 0a7 7 0 0 0-7 7c0 5 7 11 7 11s7-6 7-11a7 7 0 0 0-7-7zm0 10a3 3 0 1 1 0-6 3 3 0 0 1 0 6z" fill="#fff"/></svg></span>
    <span>240 Harbor Crest Lane<br>Suite 300 Coral Point, Florida 33100</span>
  </div>
  <div class="contact-row" style="margin-top:14px;align-items:center">
    <span class="contact-icon"><svg width="16" height="16" viewBox="0 0 16 16"><path d="M3 1l3 3-2 2c1 2 3 4 5 5l2-2 3 3-2 3C6 15 1 10 0 3z" fill="#fff"/></svg></span>
    <span>(555) 010-0100</span>
  </div>
  <div class="contact-row" style="margin-top:14px;align-items:center">
    <span class="contact-icon"><svg width="16" height="12" viewBox="0 0 16 12"><rect width="16" height="12" fill="#fff"/><path d="M0 0l8 7 8-7" fill="none" stroke="#f2521c" stroke-width="1.5"/></svg></span>
    <span>hello@havenguard.example</span>
  </div>
</div>
<div class="abs" style="left:780px;top:4072px">
  <div class="foot-title">SUBSCRIBE TO NEWSLETTER</div>
  <p class="foot-text" style="width:340px;margin-top:22px">Monthly notes on infection control for senior living operators.</p>
</div>
<div class="news-input abs">Enter Your Email</div>
<div class="news-btn abs"><svg width="22" height="22" viewBox="0 0 22 22"><path d="M1 10L21 1 13 21l-3-8z" fill="#fff"/></svg></div>
<p class="copyright abs">© 2020 All Rights Reserved | Privacy Policy | Terms and Conditions | Accessibility</p>

</body>
</html>
```